Property lawyer needs a website for new law firm Sydney

WHO AM I ?
I am a real estate development lawyer based in suburban Sydney Australia with over 14 years experience and have recently started my own law firm "Bramblewood Legal". The firm is just me (a female) at this stage. I need a website designed that is capable of being edited by me frequently (hoping this is easily done?!) and can be published with the domain name I own - www.bramblewoodlegal.com.au.
My areas of practice are:
* Property development (strata & community titling, due diligence, easements, by-laws and management statements, structuring etc)
* Conveyancing (sale and purchase of residential, commercial and retail property)
* General property law (caveats, transfers, related party transactions, easements, leases, powers of attorney etc).
WEBSITE REQUIREMENTS
I would like a website which conveys professionalism, has a fresh modern corporate look and is easy to navigate. The website will mostly be accessed by potential clients looking for information about me, my areas of practice and how to get in contact with me. My potential clients are corporate developers and individuals who are buying and selling property.
My logo for Bramblewood Legal (see attached) is simple, clean and professional looking. I would like the website to work with the logo without being too dark.
I haven't written all of the content yet, so please use filler text for everything and structure the menus as described above. The site will need to be capable of being updated and edited by me.
Other than that I will leave the design up to you.
Thanks and happy designing!
Target Market(s)
Professional developers and individuals buying and selling real estate
Industry/Entity Type
Real Estate
Coding
Coded - Design and coding required
Number of Pages Required
4 page
Requirements
Must have
- I would like a website which conveys professionalism, has a fresh modern corporate look and is easy to navigate. The website will mostly be accessed by potential clients looking for information about me, my areas of practice and how to get in contact with me. My potential clients are corporate developers and individuals who are buying and selling property.
- Please use my logo for Bramblewood Legal. I would like the website to work with the logo - the colours are a dark blue (C 100% M 50% B 50%) and grey (C10% B 40%). I don't want the website to be too dark though.
- I am thinking 4 pages. I would like links across the top of the page for "Practice Areas", "About us" and "Contact us" - these should lead to separate landing pages with the content to be inserted later.
- The contact page should contain space for a potential client to send an email enquiry to the following email address "enquiries@bramblewoodlegal.com.au". My contact details are set out in the attached letterhead (see attached).
- I would also like the home page to set out what my three Practice Areas are - Property Development; Conveyancing; General Property Law. Each area should have some filler text under it which will be completed later and a link to be able to take me to the "Practice Areas" page where more detail on each will be provided.
- Please select images that are relevant to my practice as a property lawyer. The photos you use will be the ones which I use so please choose wisely.
- I will need a link on the bottom of the home page showing that I am a member of "The Counsel Guild of NSW" (see attached logo).
- The bottom of each page should also include the following statement "Bramblewood Legal is a business name of Bramblewood Legal Pty Limited ACN 482 517 306, an incorporated legal practice regulated by the Legal Profession Act 2004. Liability limited by a scheme approved under the Professional Standards Legislation."
Nice to have
- Have attached an image of me (not the best) but at least its me. Consider whether to use on "About us" page
Should not have
- No images of gavels, scales of justice or law books.
- Images not to be too masculine
- Website not to be too dark

```html
<!DOCTYPE html>
<html lang="en">
<head>
<meta charset="utf-8">
<title>Bramblewood Legal — Property Lawyer, Sydney</title>
<link href="https://fonts.googleapis.com/css2?family=Tinos:wght@400;700&family=Open+Sans:wght@400;600&display=swap" rel="stylesheet">
<style>
:root{
  --navy:#0b3c6e;
  --navy-deep:#082d54;
  --title-light:#c7d6e8;
  --ink:#1d1d1d;
  --grey:#6f7378;
  --panel:#f1f2f4;
  --line:#c9ccd1;
  --white:#ffffff;
  --hero-a:#2a2c30;
  --hero-b:#6b6e73;
  --badge:#c9372c;
}
*{box-sizing:border-box;margin:0;padding:0}
html,body{width:1200px;height:2516px;overflow:hidden}
body{position:relative;background:var(--white);font-family:"Open Sans",Arial,sans-serif;color:var(--ink)}

/* hero */
.hero{position:absolute;left:0;top:0;width:1200px;height:604px;background:linear-gradient(120deg,var(--hero-a),var(--hero-b) 55%,#3a3c40)}
.brand{position:absolute;top:34px;width:100%;text-align:center;font-family:"Tinos",serif;font-size:72px;letter-spacing:1px;color:var(--title-light);line-height:1;white-space:nowrap}
.nav{position:absolute;top:126px;width:100%;display:flex;justify-content:center;gap:40px;font-size:14px;font-weight:600;color:var(--white);letter-spacing:.5px}
.hero-box{position:absolute;left:320px;top:214px;width:580px;padding:22px 28px;background:rgba(10,12,16,.72)}
.hero-box h1{font-family:"Tinos",serif;font-size:26px;line-height:1.25;color:var(--white)}
.hero-box p{margin-top:10px;font-size:13px;line-height:1.55;color:#b9bcc0}
.arrows{position:absolute;left:528px;top:458px;display:flex;gap:8px}
.arrow{width:64px;height:64px;background:rgba(0,0,0,.55);border:1px solid rgba(255,255,255,.35);display:flex;align-items:center;justify-content:center}

/* section titles */
.sec-title{position:absolute;width:100%;text-align:center;font-family:"Tinos",serif;font-size:36px;color:var(--navy);letter-spacing:.5px}
.rule{position:absolute;left:574px;width:52px;height:2px;background:var(--navy)}
.intro{position:absolute;top:802px;left:300px;width:600px;text-align:center;font-family:"Tinos",serif;font-size:22px;line-height:1.4;color:var(--navy)}
.intro-small{position:absolute;top:886px;width:100%;text-align:center;font-size:13px;color:var(--grey)}

/* practice rows */
.row{position:absolute;left:0;width:1200px;height:220px;display:flex}
.photo{width:600px;height:220px}
.panel{width:600px;height:220px;padding:40px 40px}
.panel h3{font-family:"Tinos",serif;font-size:24px;font-weight:400}
.panel p{margin-top:10px;font-size:13px;line-height:1.55;width:440px}
.btn{display:inline-block;margin-top:22px;padding:9px 0;width:172px;text-align:center;font-size:11px;letter-spacing:1px}
.panel.light{background:var(--panel)}
.panel.light h3{color:var(--navy)}
.panel.light p{color:var(--grey)}
.panel.light .btn{border:1px solid var(--line);color:var(--grey);background:var(--white)}
.panel.dark{background:var(--navy)}
.panel.dark h3,.panel.dark p{color:var(--white)}
.panel.dark .btn{border:1px solid rgba(255,255,255,.7);color:var(--white)}

/* contact */
.contact{position:absolute;top:1828px;left:0;width:1200px;height:376px;display:flex}
.map{position:relative;width:600px;height:376px;background:linear-gradient(135deg,#e8e5dc,#d9dde0 60%,#e6e1d4)}
.card{position:absolute;left:176px;top:128px;width:264px;padding:14px 16px;background:var(--white);box-shadow:0 2px 6px rgba(0,0,0,.2)}
.card .name{font-family:"Tinos",serif;font-size:16px;color:var(--navy);white-space:nowrap}
.card li{list-style:none;margin-top:6px;font-size:10px;color:var(--grey);white-space:nowrap}
.form{width:600px;height:376px;background:var(--navy);padding:48px 0 0 36px}
.field{display:flex;width:378px;height:42px;margin-bottom:16px;background:var(--white)}
.field .ico{width:42px;background:#e3e6ea;display:flex;align-items:center;justify-content:center}
.field span{padding:12px;font-size:11px;color:#9ea3a8}
.field.tall{height:88px}
.send{margin-left:42px;width:336px;padding:10px 0;text-align:center;border:1px solid rgba(255,255,255,.7);color:var(--white);font-size:11px;letter-spacing:1px}

/* footer */
.member{position:absolute;top:2262px;width:100%;display:flex;justify-content:center;align-items:center;gap:10px}
.member .mark{width:34px;height:34px;background:var(--badge)}
.member .name{font-size:12px;font-weight:600;color:var(--badge);width:110px;line-height:1.3}
.follow{position:absolute;top:2358px;width:100%;text-align:center;font-size:13px;letter-spacing:1px;color:var(--navy);font-weight:600}
.social{position:absolute;top:2392px;width:100%;display:flex;justify-content:center;gap:12px}
.social i{display:block;width:30px;height:30px;border-radius:50%;background:#8a8f96}
.legal{position:absolute;top:2440px;left:200px;width:800px;text-align:center;font-size:9px;color:var(--grey);line-height:1.4}
.bottom{position:absolute;top:2478px;left:0;width:1200px;height:38px;background:var(--navy-deep);color:#aeb7c2;font-size:10px;text-align:center;line-height:38px}
</style>
</head>
<body>

<header class="hero" role="img" aria-label="Photograph of a lawyer's desk with signed property documents">
  <div class="brand">BRAMBLEWOOD LEGAL</div>
  <nav class="nav"><span>HOME</span><span>PRACTICE AREAS</span><span>WHO WE ARE</span><span>CONTACT US</span></nav>
  <div class="hero-box">
    <h1>We're the real estate development lawyer based in suburban Sydney Australia.</h1>
    <p>Our core services are residential and property development, conveyancing, general property law.</p>
  </div>
  <div class="arrows">
    <div class="arrow"><svg width="14" height="20" viewBox="0 0 14 20"><path d="M11 2 3 10l8 8" fill="none" stroke="#fff" stroke-width="3"/></svg></div>
    <div class="arrow"><svg width="14" height="20" viewBox="0 0 14 20"><path d="M3 2l8 8-8 8" fill="none" stroke="#fff" stroke-width="3"/></svg></div>
  </div>
</header>

<h2 class="sec-title" style="top:700px">PRACTICE AREAS</h2>
<div class="rule" style="top:750px"></div>
<p class="intro">We're the real estate development lawyer based in Suburban Sydney Australia.</p>
<p class="intro-small">Our practice areas include:</p>

<section class="row" style="top:956px">
  <div class="photo" role="img" aria-label="Photograph of hands holding a small model house" style="background:linear-gradient(135deg,#2f6fae,#a9c8e6 60%,#dbe7f2)"></div>
  <div class="panel light">
    <h3>Property Development</h3>
    <p>Strata &amp; Community Titling, Due Diligence, Easements, By-Laws and Management Statements, Structuring etc.</p>
    <span class="btn">LEARN MORE</span>
  </div>
</section>

<section class="row" style="top:1176px">
  <div class="panel dark">
    <h3>Conveyancing</h3>
    <p>Sale and Purchase of Residential, Commercial and Retail Property.</p>
    <span class="btn">LEARN MORE</span>
  </div>
  <div class="photo" role="img" aria-label="Photograph of a professional meeting in an office" style="background:linear-gradient(135deg,#7a5f4c,#c9b7a6 55%,#e9e4df)"></div>
</section>

<section class="row" style="top:1396px">
  <div class="photo" role="img" aria-label="Photograph of a pen signing a contract" style="background:linear-gradient(135deg,#5c6f86,#c5ced8 60%,#eef1f4)"></div>
  <div class="panel light">
    <h3>General Property Law</h3>
    <p>Caveats, Transfers, Related Party Transactions, Easements, Leases, Powers of Attorney etc.</p>
    <span class="btn">LEARN MORE</span>
  </div>
</section>

<h2 class="sec-title" style="top:1716px">GET IN TOUCH</h2>
<div class="rule" style="top:1766px"></div>

<section class="contact">
  <div class="map" role="img" aria-label="Street map showing the office location in suburban Sydney">
    <svg style="position:absolute;left:150px;top:92px" width="20" height="28" viewBox="0 0 20 28"><path d="M10 0a10 10 0 0 0-10 10c0 7 10 18 10 18s10-11 10-18A10 10 0 0 0 10 0z" fill="#d6372b"/><circle cx="10" cy="10" r="4" fill="#fff"/></svg>
    <div class="card">
      <div class="name">BRAMBLEWOOD LEGAL</div>
      <ul>
        <li>14 Wattle Grove Road, Parramatta NSW 2150</li>
        <li>enquiries@bramblewoodlegal.com.au</li>
        <li>(02) 9000 4417</li>
      </ul>
    </div>
  </div>
  <form class="form">
    <div class="field"><div class="ico"><svg width="16" height="16" viewBox="0 0 16 16"><circle cx="8" cy="5" r="3.5" fill="#0b3c6e"/><path d="M1 16c0-4 3-6 7-6s7 2 7 6z" fill="#0b3c6e"/></svg></div><span>Enter your name</span></div>
    <div class="field"><div class="ico"><svg width="16" height="12" viewBox="0 0 16 12"><rect width="16" height="12" fill="#0b3c6e"/><path d="M0 0l8 7 8-7" fill="none" stroke="#fff" stroke-width="1.5"/></svg></div><span>Enter your email address</span></div>
    <div class="field"><div class="ico"><svg width="14" height="16" viewBox="0 0 14 16"><path d="M3 0h3l1 4-2 1.5c1 2 2 3 3.5 4L10 7.5l4 1v3c0 2-1.5 3-3.5 3C5 14 0 9 0 3.5 0 1.5 1 0 3 0z" fill="#0b3c6e"/></svg></div><span>Enter your phone</span></div>
    <div class="field tall"><div class="ico"><svg width="16" height="16" viewBox="0 0 16 16"><path d="M2 14l1-4 8-8 3 3-8 8z" fill="#0b3c6e"/></svg></div><span>Your message</span></div>
    <div class="send">SEND NOW</div>
  </form>
</section>

<div class="member">
  <div class="mark"></div>
  <div class="name">The Counsel Guild of NSW</div>
</div>
<div class="follow">FOLLOW US</div>
<div class="social"><i></i><i></i><i></i></div>
<p class="legal">Bramblewood Legal is a business name of Bramblewood Legal Pty Limited ACN 482 517 306, an incorporated legal practice regulated by the Legal Profession Act 2004. Liability limited by a scheme approved under the Professional Standards Legislation.</p>
<footer class="bottom">Copyright 2015 BRAMBLEWOOD LEGAL. All Rights Reserved.</footer>

</body>
</html>
```